Spring Anti-wrinkle Injections Poster

A1 size poster for Spring promoting anti-wrinkle injections (Lumavel)
Poster is to promote rejuvination and refreshing of the appreaance coming into the warmer months.

Please feel free to add promotional message. We want to encourage walk by traffic to have anti-wrinkle treatments.

- Poster must not be overly feminine.
- Promote Lumavel injections for smoothing and refreshing apprearance (word
lumavel can not be used please use 'Anti-wrinkle injection')

Industry/Entity Type

Promotional

Requirements
Must have
• - Logo (attached)

- 4 clinic locations with contact numbers
Suite 204, 7 Pardell Street, Melbourne 9371 5802
418 Brisket Street, Richmond 9516 7043
Shop 22 The Quarry Mall, Dandenong 9185 6037
8 Fernway Close, Mount Waverley 9242 7659

- Website
www.velarobrow-example.com

- Feel and look of poster to be targeted towards females but not overly feminine, we are a unisex clinic.
Should not have
• - The word lumavel can not be used please use 'Anti-wrinkle injection' instead

```html
<!DOCTYPE html>
<html lang="en">
<head>
<meta charset="utf-8">
<title>Spring Anti-wrinkle Injection Poster</title>
<link rel="stylesheet" href="https://fonts.googleapis.com/css2?family=Alfa+Slab+One&family=Archivo+Black&family=Arimo:wght@400;700&family=Kaushan+Script&display=swap">
<style>
  :root {
    --canvas-black: #000000;
    --outline-dark: #111111;
    --blossom-pink: #f2a6e6;
    --blossom-deep: #b88ac8;
    --sky-haze: #d9c2e6;
    --grass-green: #6aa83a;
    --grass-deep: #3f7a22;
    --spring-pink: #f7a8ec;
    --wrinkle-cyan: #22f0f4;
    --injection-red: #ff2a00;
    --soft-green: #a6f08a;
    --script-shade: #1d3a10;
    --band-red: #a8262a;
    --clinic-red: #ff1a1a;
    --white: #ffffff;
    --lime: #a4f542;
    --title-lilac: #e6e6f0;
    --info-grey: #4a4a4a;
    --logo-ink: #7a3a8a;
  }
  html, body {
    margin: 0;
    padding: 0;
    width: 812px;
    height: 1200px;
    overflow: hidden;
    background: var(--canvas-black);
  }
  .poster {
    position: relative;
    width: 812px;
    height: 1200px;
    background: var(--canvas-black);
    font-family: "Arimo", Arial, sans-serif;
  }
  .hero-photo {
    position: absolute;
    left: 30px;
    top: 30px;
    width: 745px;
    height: 681px;
    background:
      linear-gradient(180deg,
        var(--sky-haze) 0%,
        var(--blossom-pink) 22%,
        var(--blossom-deep) 45%,
        var(--grass-green) 72%,
        var(--grass-deep) 100%);
  }
  .brand-mark {
    position: absolute;
    left: 296px;
    top: 71px;
    width: 237px;
    height: 98px;
    background: var(--white);
    border: 3px solid #222;
    box-sizing: border-box;
    display: flex;
    align-items: center;
    justify-content: center;
    font-family: "Arimo", Arial, sans-serif;
    font-weight: 400;
    font-size: 20px;
    color: var(--logo-ink);
    text-align: center;
    z-index: 2;
  }
  .headline {
    position: absolute;
    left: 30px;
    width: 745px;
    margin: 0;
    text-align: center;
    line-height: 1;
    paint-order: stroke fill;
    white-space: nowrap;
  }
  .headline-spring {
    top: 182px;
    font-family: "Alfa Slab One", Georgia, serif;
    font-size: 146px;
    letter-spacing: 6px;
    color: var(--spring-pink);
    transform: scaleX(1.25);
    transform-origin: center;
    text-shadow:
      3px 0 0 var(--outline-dark), -3px 0 0 var(--outline-dark),
      0 3px 0 var(--outline-dark), 0 -3px 0 var(--outline-dark),
      2px 2px 0 var(--outline-dark), -2px 2px 0 var(--outline-dark),
      2px -2px 0 var(--outline-dark), -2px -2px 0 var(--outline-dark);
  }
  .headline-product {
    top: 348px;
    font-family: "Archivo Black", Arial, sans-serif;
    font-size: 92px;
    color: var(--wrinkle-cyan);
    -webkit-text-stroke: 6px var(--outline-dark);
  }
  .headline-treatment {
    top: 430px;
    font-family: "Archivo Black", Arial, sans-serif;
    font-size: 128px;
    color: var(--injection-red);
    -webkit-text-stroke: 8px var(--outline-dark);
  }
  .subline-benefit {
    top: 548px;
    font-family: "Arimo", Arial, sans-serif;
    font-size: 70px;
    color: var(--soft-green);
  }
  .subline-result {
    top: 625px;
    font-family: "Kaushan Script", cursive;
    font-size: 56px;
    color: var(--soft-green);
    -webkit-text-stroke: 4px var(--script-shade);
  }
  .unisex-band {
    position: absolute;
    left: 30px;
    top: 711px;
    width: 745px;
    height: 119px;
    background: var(--band-red);
    display: flex;
    align-items: center;
    justify-content: center;
  }
  .unisex-message {
    margin: 0;
    font-family: "Archivo Black", Arial, sans-serif;
    font-size: 56px;
    color: var(--clinic-red);
    -webkit-text-stroke: 7px var(--white);
    paint-order: stroke fill;
  }
  .locations {
    position: absolute;
    left: 30px;
    top: 830px;
    width: 745px;
    height: 322px;
    background: linear-gradient(180deg, var(--info-grey) 0%, #2a2a2a 55%, #111 100%);
    box-shadow: inset 0 -30px 40px #000;
  }
  .locations-title {
    position: absolute;
    left: 18px;
    top: 14px;
    margin: 0;
    font-weight: 700;
    font-size: 32px;
    color: var(--title-lilac);
  }
  .location-list {
    list-style: none;
    margin: 0;
    padding: 0;
    position: absolute;
    left: 18px;
    top: 62px;
    width: 715px;
  }
  .location-list li {
    font-weight: 700;
    font-size: 27px;
    color: var(--lime);
    line-height: 48px;
    white-space: nowrap;
  }
  .website {
    position: absolute;
    left: 0;
    top: 252px;
    width: 745px;
    margin: 0;
    text-align: center;
    font-weight: 700;
    font-size: 21px;
    color: var(--lime);
  }
  .bottom-rule {
    position: absolute;
    left: 30px;
    top: 1152px;
    width: 745px;
    height: 4px;
    background: var(--band-red);
  }
</style>
</head>
<body>
  <main class="poster">
    <div class="hero-photo" role="img" aria-label="Cherry blossom trees in full pink bloom over a green spring lawn"></div>

    <div class="brand-mark">Harlow Dermal Studio</div>

    <h1 class="headline headline-spring">spring</h1>
    <p class="headline headline-product">anti-wrinkle</p>
    <p class="headline headline-treatment">injection</p>
    <p class="headline subline-benefit">for smoothing and</p>
    <p class="headline subline-result">refreshing appearance</p>

    <section class="unisex-band">
      <p class="unisex-message">we are unisex clinic</p>
    </section>

    <section class="locations">
      <h2 class="locations-title">4 Office Locations:</h2>
      <ul class="location-list">
        <li>Suite 204, 7 Pardell Street, Melbourne 9371 5802</li>
        <li>418 Brisket Street, Richmond 9516 7043</li>
        <li>Shop 22 The Quarry Mall, Dandenong 9185 6037</li>
        <li>8 Fernway Close, Mount Waverley 9242 7659</li>
      </ul>
      <p class="website">website: www.velarobrow-example.com</p>
    </section>

    <div class="bottom-rule"></div>
  </main>
</body>
</html>
```